A4 6 page tri-fold brochure for security screen company

Brochure design and layout for a new company based in the UAE called Harbor Panes. We make clear mesh security screen doors and windows that aesthetically blend with the house, like a fly screen, rather than a traditional heavy looking security screen. We want to project an image of safety and security but with warmth and humanity to it, not just something clinical. Copy hasn't been written yet so use dummy text or pull and adjust copy form our website www.harborpanes-example.ae.
Target market: home owners, financially comfortable, possibly with young children or pets.
Purpose of brochure: to have potential clients contact us (via phone, whatsapp, email or through our website) to arrange a free measure and quote.
More details provided in attached word doc brief and product images, logos etc, attached also.
Please see attached brief.

Target Market(s)

Home owners, financially comfortable, possibly with young children or pets.

Industry/Entity Type

Home Improvement

Font styles to use
Serif
Sans Serif

Colors
0255a3
3176b5
85acd3
cfdfed
eaf1f7

Requirements
Must have
• Good clear images with detailed close ups (or call outs) of specific details such as the mesh and locks.
• Contact details to include website www.harborpanes-example.ae, phone number: +971 50 318 2097, email address: oliver@harborpanes-example.ae
Nice to have
• If your are comfortable using and adjusting the appropriate copy from our website please do so.
• Images - I've included a lot of images so please choose the most appropriate to help sell the product. Some of the better images I like are: _DSC2929, French_Windows, HARBOR_PANES-3204, HARBOR_PANES-3231, HARBOR_PANES-3345, HARBOR_PANES-3354, HARBOR_PANES-3401, Girls room windows1, Girls room windows2, IMG_2968. Please don't limit yourself to these images and use the ones you feel best fit.
Should not have
• Please see attached brief.

```html
<!DOCTYPE html>
<html lang="en">
<head>
<meta charset="utf-8">
<title>Harbor Panes – Tri-fold Brochure Outside</title>
<link href="https://fonts.googleapis.com/css2?family=Raleway:wght@300;400;500;600;700;800&display=swap" rel="stylesheet">
<style>
  :root{
    --blue-deep:#0255a3;
    --blue:#3176b5;
    --blue-bright:#2f8ae6;
    --blue-soft:#85acd3;
    --blue-pale:#cfdfed;
    --blue-mist:#eaf1f7;
    --navy:#0b2b5c;
    --charcoal:#1d1f23;
    --charcoal-2:#2a2c31;
    --text:#4a4d52;
    --text-light:#c9ccd1;
    --gold:#f1d9a0;
    --white:#ffffff;
    --stage:#5b5c5e;
  }
  *{margin:0;padding:0;box-sizing:border-box}
  html,body{width:1200px;height:712px;overflow:hidden;background:var(--stage);font-family:"Raleway",sans-serif}
  .brochure{position:absolute;left:0;top:73px;width:1200px;height:566px;background:var(--white);overflow:hidden}
  .layer{position:absolute;left:0;top:0;width:1200px;height:566px}
  .abs{position:absolute}
  .h-section{font-size:15px;font-weight:400;color:#1f2126;letter-spacing:.2px}
  .h-section b{font-weight:800;color:var(--blue-deep)}
  .body-copy{font-size:6.6px;line-height:9.6px;color:var(--text);text-align:justify}
  .test-list{list-style:none;font-size:6.8px;line-height:10.5px;color:var(--blue-deep)}
  .test-list li::before{content:"•";margin-right:5px;color:var(--blue-deep)}
  .contact-prompt{font-size:14.5px;color:var(--blue);font-weight:400}
  .contact-sub{font-size:7.8px;color:var(--text)}
  .warranty-title{font-size:15.5px;font-weight:700;color:var(--gold);letter-spacing:.3px}
  .rule{height:1.5px;background:var(--white);width:34px}
  .warranty-copy{font-size:6.6px;line-height:9.6px;color:var(--text-light);text-align:justify}
  .url-strong{font-size:12.5px;font-weight:700;color:var(--white)}
  .center{text-align:center}
  .kicker{font-size:11px;color:#55585d;letter-spacing:.2px}
  .headline{font-size:13.2px;font-weight:800;color:var(--blue-deep);line-height:17px}
  .intro-copy{font-size:7.8px;line-height:11.8px;color:var(--text)}
  .quote-mark{font-size:52px;font-weight:800;color:#b9bcc0;line-height:40px}
  .quote-copy{font-size:7.8px;line-height:12.5px;color:var(--text)}
  .quote-by{font-size:7.2px;color:var(--blue)}
  .quote-by b{font-weight:800;color:var(--blue-deep)}
  .contact-title{font-size:16px;font-weight:700;color:var(--white);letter-spacing:.4px}
  .contact-title span{display:inline-block;width:22px;height:1.5px;background:var(--white);vertical-align:middle;margin:0 6px}
  .contact-copy{font-size:6.5px;line-height:9.4px;color:var(--blue-pale)}
  .phone{font-size:17px;font-weight:800;color:var(--white)}
  .contact-line{font-size:10.5px;color:var(--white);font-weight:500}
  .wordmark{font-size:29px;font-weight:700;color:var(--blue-deep);letter-spacing:2px;display:flex;align-items:center;gap:10px}
  .wordmark i{display:block;width:22px;height:22px;background:var(--blue-deep)}
  .mid-name{font-size:15px;font-weight:700;color:var(--white);letter-spacing:2px}
  .cover-kicker{font-size:17px;font-weight:400;color:var(--white);letter-spacing:5px}
  .cover-title{font-size:20px;font-weight:800;color:var(--blue-bright);letter-spacing:.3px}
  .cover-line{font-size:14px;color:var(--white);font-weight:400;line-height:21px}
  .cover-line b{font-weight:700;font-size:15px}
  .cover-url{font-size:8px;color:var(--text-light);letter-spacing:1px}
  .icon{display:inline-block;vertical-align:middle;margin-right:5px}
</style>
</head>
<body>
<div class="brochure">

  <!-- Shapes, bands and image areas -->
  <svg class="layer" viewBox="0 0 1200 566" xmlns="http://www.w3.org/2000/svg">
    <defs>
      <linearGradient id="g-cat" x1="0" y1="0" x2="1" y2="1">
        <stop offset="0" stop-color="#dfe3e6"/><stop offset="1" stop-color="#b59873"/>
      </linearGradient>
      <linearGradient id="g-mesh" x1="0" y1="0" x2="0" y2="1">
        <stop offset="0" stop-color="#06142e"/><stop offset=".5" stop-color="#1f6fd1"/><stop offset="1" stop-color="#06142e"/>
      </linearGradient>
      <linearGradient id="g-window" x1="0" y1="0" x2="1" y2="1">
        <stop offset="0" stop-color="#e6ebef"/><stop offset="1" stop-color="#8d9aa5"/>
      </linearGradient>
      <linearGradient id="g-door" x1="0" y1="0" x2="1" y2="0">
        <stop offset="0" stop-color="#7fa8a0"/><stop offset=".5" stop-color="#dfe6ea"/><stop offset="1" stop-color="#8fae84"/>
      </linearGradient>
      <linearGradient id="g-dark" x1="0" y1="0" x2="0" y2="1">
        <stop offset="0" stop-color="#2b2d32"/><stop offset="1" stop-color="#18191c"/>
      </linearGradient>
      <linearGradient id="g-blue" x1="0" y1="0" x2="0" y2="1">
        <stop offset="0" stop-color="#1a5fb0"/><stop offset="1" stop-color="#0a2f66"/>
      </linearGradient>
      <radialGradient id="g-seal" cx=".5" cy=".4" r=".6">
        <stop offset="0" stop-color="#f4d27a"/><stop offset="1" stop-color="#b98320"/>
      </radialGradient>
    </defs>

    <!-- Panel 1 -->
    <polygon points="0,0 170,0 177,95 142,172 0,172" fill="url(#g-cat)" role="img" aria-label="Photo of a cat sitting behind a mesh screen door"/>
    <polygon points="313,212 349,192 385,212 385,318 349,340 313,318 246,318 246,212" fill="none"/>
    <polygon points="313,190 383,228 383,305 313,343 244,305 244,228" fill="url(#g-mesh)" stroke="#e4e7ea" stroke-width="4" role="img" aria-label="Close-up of stainless steel mesh lit in blue"/>
    <polygon points="0,359 352,359 400,402 400,566 0,566" fill="url(#g-dark)"/>
    <polygon points="352,359 366,359 400,390 400,402" fill="#e9ebed"/>
    <circle cx="322" cy="478" r="52" fill="url(#g-seal)" role="img" aria-label="Gold warranty seal"/>
    <circle cx="322" cy="478" r="42" fill="none" stroke="#8a5c12" stroke-width="1.5"/>

    <!-- Panel 2 -->
    <rect x="400" y="0" width="400" height="359" fill="var(--white)"/>
    <line x1="400" y1="203" x2="450" y2="203" stroke="#b8bcc1" stroke-dasharray="2 2" stroke-width=".8"/>
    <line x1="752" y1="203" x2="800" y2="203" stroke="#b8bcc1" stroke-dasharray="2 2" stroke-width=".8"/>
    <g role="img" aria-label="Photos of screened windows and doors in diamond frames" stroke="#ffffff" stroke-width="3">
      <polygon points="509,108 571,170 509,232 447,170" fill="url(#g-window)"/>
      <polygon points="600,126 652,178 600,230 548,178" fill="url(#g-window)"/>
      <polygon points="690,110 724,144 690,178 656,144" fill="#d7d9dc"/>
      <polygon points="730,150 770,190 730,230 690,190" fill="url(#g-window)"/>
    </g>
    <polyline points="436,256 436,326 758,326 758,256" fill="none" stroke="#b8bcc1" stroke-dasharray="2 2" stroke-width=".8"/>
    <rect x="400" y="359" width="400" height="207" fill="var(--navy)"/>
    <polygon points="400,412 600,378 800,412 800,566 400,566" fill="url(#g-blue)"/>
    <polygon points="400,404 600,370 800,404 800,412 600,378 400,412" fill="#e9ebed"/>

    <!-- Panel 3 -->
    <rect x="800" y="91" width="400" height="300" fill="url(#g-door)" role="img" aria-label="Photo of a young child looking through a security screen door onto a garden"/>
    <polygon points="800,356 1200,424 1200,566 800,566" fill="url(#g-dark)"/>
    <polygon points="900,362 1200,403 1200,412 900,370" fill="#e9ebed"/>
    <line x1="1170" y1="472" x2="1246" y2="472" stroke="#fff"/>
    <line x1="1180" y1="472" x2="1254" y2="472" stroke="#fff"/>
  </svg>

  <!-- Panel 1 content -->
  <h2 class="abs h-section" style="left:193px;top:8px">PRODUCT <b>TESTING</b></h2>
  <p class="abs body-copy" style="left:193px;top:40px;width:188px">All Harbor Panes products have been designed, manufactured and tested in accordance with strict Australian Security Standards. The screens exceeded the following Australian Security Standards (AS 5039 and 5041) tests:</p>
  <ul class="abs test-list" style="left:200px;top:99px">
    <li>Knife Shear Test</li>
    <li>Dynamic Impact Test</li>
    <li>Lock and Hinge Lever (Jimmy) Test</li>
    <li>Salt Spray Test</li>
  </ul>

  <h2 class="abs h-section" style="left:9px;top:190px">FLY <b>SCREEN REPAIR</b></h2>
  <p class="abs body-copy" style="left:11px;top:224px;width:224px">Genuine Harbor Panes mesh screens are constructed from finely woven strands of stainless steel. The strands are only 0.8mm thick but spaced to ensure flies and mosquitoes can't pass through. A normal fly screen can be cut with a knife, ripped by a cat or pushed in by a child. Harbor Panes mesh door and window screens pass the Australian Standards 5041 Knife Shear and impact tests. The door and window screens are also resistant to crow bar attack, puncture and tearing.</p>
  <p class="abs contact-prompt" style="left:12px;top:313px">Please contact us</p>
  <p class="abs contact-sub" style="left:12px;top:331px">for a free measure and quote.</p>

  <h2 class="abs warranty-title" style="left:12px;top:396px">10 YEAR WARRANTY</h2>
  <div class="abs rule" style="left:12px;top:419px"></div>
  <p class="abs warranty-copy" style="left:12px;top:428px;width:252px">Harbor Panes are manufactured to the highest quality controlled standards by an ISO 9001 certified company. The high tensile, woven, stainless steel mesh has been powdered coated and tested to resist the harsh Middle East elements. With a very small amount of maintenance, your Harbor Panes will resist the elements and maintain their great look for years to come.</p>
  <p class="abs warranty-copy" style="left:12px;top:503px;width:252px">Should you have any problems with your Harbor Panes, we offer a 10 year warranty on all stainless steel mesh and aluminium products and 1 year on component parts.</p>
  <p class="abs url-strong" style="left:14px;top:542px">www.harborpanes-example.ae</p>

  <!-- Panel 2 content -->
  <p class="abs kicker center" style="left:400px;top:12px;width:400px">SUPER STRONG, STAINLESS STEEL MESH</p>
  <h1 class="abs headline center" style="left:400px;top:26px;width:400px">SECURITY SCREENS THAT LOOK STYLISH<br>AND WON'T BREAK.</h1>
  <div class="abs" style="left:581px;top:64px;width:38px;height:1px;background:var(--blue)"></div>
  <p class="abs intro-copy center" style="left:420px;top:72px;width:360px">Harbor Panes are a brand new initiative to the UAE. We custom make and install premium high grade stainless steel mesh screen doors and window screens in place of those flimsy fly screens we know drive you crazy.</p>
  <div class="abs quote-mark" style="left:448px;top:250px">&ldquo;</div>
  <p class="abs quote-copy center" style="left:446px;top:274px;width:302px">Great product &amp; service. High quality. With this product securing access, allowing fresh air in but keeping the bugs out, I am happy to leave my child's patio door open at night during cool evenings.</p>
  <p class="abs quote-by" style="right:418px;top:319px"><b>MARCUS</b> – Palm Grove, Dubai</p>

  <p class="abs mid-name center" style="left:400px;top:386px;width:400px">HARBOR PANES</p>
  <h2 class="abs contact-title center" style="left:400px;top:451px;width:400px"><span></span>CONTACT US<span></span></h2>
  <p class="abs contact-copy center" style="left:430px;top:477px;width:340px">Please feel free to contact us by completing the email form below or call us if you have any questions or would like to arrange a free measure and quote.</p>
  <p class="abs phone center" style="left:400px;top:503px;width:400px">
    <svg class="icon" width="13" height="13" viewBox="0 0 24 24"><circle cx="12" cy="12" r="11" fill="none" stroke="#fff" stroke-width="2"/><path d="M8 6.5l2 0 1 3-1.4 1.2a7 7 0 0 0 3.7 3.7L14.5 13l3 1v2c0 .8-.7 1.5-1.5 1.5A10 10 0 0 1 6.5 8c0-.8.7-1.5 1.5-1.5z" fill="#fff"/></svg>+971 50 318 2097</p>
  <p class="abs contact-line center" style="left:400px;top:525px;width:400px">
    <svg class="icon" width="10" height="10" viewBox="0 0 24 24"><circle cx="12" cy="12" r="10" fill="none" stroke="#fff" stroke-width="2.5"/><rect x="7" y="8.5" width="10" height="7" fill="none" stroke="#fff" stroke-width="1.8"/><path d="M7 8.5l5 4 5-4" fill="none" stroke="#fff" stroke-width="1.8"/></svg>oliver@harborpanes-example.ae</p>
  <p class="abs contact-line center" style="left:400px;top:541px;width:400px">
    <svg class="icon" width="10" height="10" viewBox="0 0 24 24"><circle cx="12" cy="12" r="10" fill="none" stroke="#fff" stroke-width="2.5"/><ellipse cx="12" cy="12" rx="4" ry="10" fill="none" stroke="#fff" stroke-width="1.8"/><line x1="2" y1="12" x2="22" y2="12" stroke="#fff" stroke-width="1.8"/></svg>www.harborpanes-example.ae</p>

  <!-- Panel 3 content -->
  <div class="abs wordmark" style="left:860px;top:30px"><i></i>HARBOR PANES</div>
  <p class="abs cover-kicker center" style="left:800px;top:425px;width:400px">SECURITY SCREEN</p>
  <h1 class="abs cover-title center" style="left:800px;top:445px;width:400px">DOORS AND WINDOWS</h1>
  <div class="abs" style="left:983px;top:473px;width:34px;height:1px;background:var(--white)"></div>
  <p class="abs cover-line center" style="left:800px;top:480px;width:400px">STRONG SCREENS THAT LET THE<br><b>BREEZE IN AND KEEP INTRUDERS<br>(AND BUGS) OUT!</b></p>
  <p class="abs cover-url center" style="left:800px;top:548px;width:400px">www.harborpanes-example.ae</p>
</div>
</body>
</html>
```